Podcast cover art for Steady Footing Podcast for Busy Mothers

I am relaunching my 3 year podcast under a new name. The podcast is called Steady Footing for Busy Mothers. The parent company is called Bright Path Living (see attached logo) and should be represented on the cover in a small way. Previously the show was called Bright Path Living. We talk about creating life balance for working moms by focusing on faith, marriage, parenting, career, health, home, finances, and friends/fun. I don't mind having stock photography on the cover but I prefer not to have my image on it as it is not a personal brand. I have attached a couple of stock images as inspiration.

Target Market(s)

working Christian moms age 30-45 income 75,000+, working full time, Christian faith, married

Industry/Entity Type

Media

Font styles to use
Serif

Requirements
Must have
• Podcast name: Steady Footing for Busy Mothers
• By: Bright Path Living (include logo)
• I also included my brand sheet for reference which includes my brand colors and fonts. Navy should be the primary with orange and gray as the accents
Should not have
• No flowers, or overly girly. My brand is more clean, preppy, and young-sophisticated.

```html
<!DOCTYPE html>
<html lang="en">
<head>
<meta charset="UTF-8">
<title>Steady Footing for Busy Mothers – Podcast Cover</title>
<link rel="stylesheet" href="https://fonts.googleapis.com/css2?family=Barlow:wght@300;400&family=Josefin+Sans:wght@300&display=swap">
<style>
  :root {
    --navy-block: #262a36;
    --black-block: #0b0b0d;
    --gray-block: #aaa5a3;
    --orange: #e8732f;
    --white: #ffffff;
    --ink: #262a36;
    --brand-gray: #c4c4c4;
    --rule: #f2f2f2;
  }
  html, body {
    margin: 0;
    padding: 0;
    width: 1200px;
    height: 1200px;
    overflow: hidden;
    background: #333;
  }
  .cover {
    position: relative;
    width: 1200px;
    height: 1200px;
    overflow: hidden;
  }
  .backdrop {
    position: absolute;
    inset: 0;
    background:
      linear-gradient(90deg, #1c2740 0%, #1f2a45 38%, rgba(60,56,56,0) 62%),
      linear-gradient(180deg, #3e3a3a 0%, #2e2b2b 100%);
  }
  .backdrop-table {
    position: absolute;
    left: 0;
    right: 0;
    bottom: 0;
    height: 150px;
    background: linear-gradient(180deg, #8fa7ab 0%, #b4c6c6 45%, #9fb4b6 100%);
  }
  .rule {
    position: absolute;
    left: 601px;
    width: 2px;
    background: var(--rule);
  }
  .rule--top { top: 45px; height: 72px; }
  .rule--bottom { top: 740px; height: 90px; }
  .title-block {
    position: absolute;
    height: 124px;
    box-sizing: border-box;
    display: flex;
    align-items: center;
    white-space: nowrap;
  }
  .title-block--lead {
    left: 376px; top: 117px; height: 124px;
    padding: 0 30px 0 36px;
    background: var(--navy-block);
    color: var(--white);
    font: 300 84px/1 "Barlow", sans-serif;
  }
  .title-block--key {
    left: 268px; top: 241px; height: 125px;
    padding: 0 48px 0 38px;
    background: var(--black-block);
    color: var(--orange);
    font: 300 112px/1 "Josefin Sans", sans-serif;
    padding-top: 14px;
  }
  .title-block--joiner {
    left: 504px; top: 366px;
    padding: 0 34px 0 36px;
    background: var(--gray-block);
    color: var(--ink);
    font: 300 84px/1 "Barlow", sans-serif;
  }
  .title-block--second {
    left: 466px; top: 492px;
    padding: 14px 44px 0 40px;
    background: var(--navy-block);
    color: var(--white);
    font: 300 112px/1 "Josefin Sans", sans-serif;
  }
  .title-block--third {
    left: 332px; top: 616px;
    padding: 14px 44px 0 54px;
    background: var(--navy-block);
    color: var(--orange);
    font: 300 112px/1 "Josefin Sans", sans-serif;
  }
  .brand {
    position: absolute;
    left: 0;
    width: 1200px;
    top: 945px;
    display: flex;
    justify-content: center;
    align-items: center;
    gap: 14px;
    color: var(--brand-gray);
    font: 300 40px/1 "Barlow", sans-serif;
    letter-spacing: 1px;
  }
  .brand-dot {
    width: 14px;
    height: 14px;
    border-radius: 50%;
    background: var(--brand-gray);
  }
</style>
</head>
<body>
  <main class="cover">
    <div class="backdrop" role="img" aria-label="Photo: a woman in a navy knit sweater and jeans wearing a wristwatch, folding a denim jacket beside a white mug and black headphones on a pale wooden table"></div>
    <div class="backdrop-table" role="img" aria-label="Pale blue painted wooden tabletop"></div>

    <span class="rule rule--top"></span>
    <h1 class="title">
      <span class="title-block title-block--lead">Steady</span>
      <span class="title-block title-block--key">FOOTING</span>
      <span class="title-block title-block--joiner">for</span>
      <span class="title-block title-block--second">BUSY</span>
      <span class="title-block title-block--third">MOTHERS</span>
    </h1>
    <span class="rule rule--bottom"></span>

    <div class="brand">
      <span class="brand-dot"></span>
      <span class="brand-name">Bright Path Living</span>
    </div>
  </main>
</body>
</html>
```